Supplement Rebranding Bottle Design

READ WORD DOCUMENT ATTACHED.
We want to rebrand our current health supplements (see below). We do want it to be modern, vibrant and appealing. Very upscale and elegant as it targets primarily women.
Bottle size: see pictures for bottle size, along with sample bottles that we like; we’re open to any bottle similar to the ones attached.
Current bottles: So ideally, we’d keep the core color on each bottle with a new branding/bottle design. But we're open to your suggestion.

Target Market(s)

mostly women but shouldn't be overly feminine

Requirements
Must have
• see bottle sizes attached

```html
<!DOCTYPE html>
<html lang="en">
<head>
<meta charset="utf-8">
<title>Supplement Label Range</title>
<link href="https://fonts.googleapis.com/css2?family=Abril+Fatface&family=Montserrat:wght@400;500&display=swap" rel="stylesheet">
<style>
  :root {
    --backdrop: #a1807b;
    --label-white: #ffffff;
    --label-tint: #eeeef0;
    --tummy-ink: #7a1010;
    --tummy-top: #6e1a1c;
    --tummy-bottom: #f01a1a;
    --blood-ink: #14147e;
    --blood-top: #1c1c9c;
    --blood-bottom: #1414f5;
    --liver-ink: #2a0f55;
    --liver-pill: #1f0d3a;
    --liver-top: #34185e;
    --liver-bottom: #9a1ee8;
    --hormone-ink: #0f4a15;
    --hormone-top: #1a501c;
    --hormone-bottom: #138a1a;
    --pill-text: #ffffff;
  }
  * { box-sizing: border-box; margin: 0; padding: 0; }
  html, body { width: 1200px; height: 720px; overflow: hidden; }
  body { background: var(--backdrop); }
  .label-range {
    width: 1200px; height: 720px;
    display: flex; align-items: center; justify-content: center; gap: 30px;
  }
  .label {
    position: relative;
    width: 260px; height: 350px;
    overflow: hidden;
    background: var(--label-white);
    color: var(--ink);
    font-family: "Montserrat", sans-serif;
  }
  .label-pattern {
    position: absolute; inset: 0;
    background: linear-gradient(160deg, var(--label-white) 0%, var(--label-tint) 100%);
  }
  .colour-sweep { position: absolute; inset: 0; width: 260px; height: 350px; }
  .label-content { position: absolute; inset: 0; }
  .product-name {
    position: absolute; left: 10px; top: 52px;
    font-family: "Abril Fatface", serif;
    font-weight: 400;
    font-size: 36px; line-height: 0.98;
    letter-spacing: 0.5px;
    color: var(--ink);
  }
  .product-claim {
    position: absolute; left: 10px;
    color: var(--ink);
  }
  .claim-lead { display: block; font-size: 19px; font-weight: 500; line-height: 1.05; letter-spacing: 0.6px; }
  .claim-detail { display: block; font-size: 14px; font-weight: 500; line-height: 1.2; letter-spacing: 0.6px; }
  .supplement-pill {
    position: absolute; left: 0;
    width: 138px; height: 13px;
    border-radius: 0 7px 7px 0;
    background: var(--pill, var(--ink));
    color: var(--pill-text);
    font-size: 9.5px; line-height: 13px; letter-spacing: 0.4px;
    padding-left: 10px;
  }
  .capsule-count {
    position: absolute; left: 10px; top: 288px;
    font-size: 11.5px; font-weight: 500; letter-spacing: 0.3px;
    color: var(--ink);
  }
  .label--tummy { --ink: var(--tummy-ink); }
  .label--blood { --ink: var(--blood-ink); }
  .label--liver { --ink: var(--liver-ink); --pill: var(--liver-pill); }
  .label--hormone { --ink: var(--hormone-ink); }
</style>
</head>
<body>
<main class="label-range">

  <article class="label label--tummy">
    <div class="label-pattern" role="img" aria-label="Faint floral line pattern across the label"></div>
    <svg class="colour-sweep" viewBox="0 0 260 350" aria-hidden="true">
      <defs>
        <linearGradient id="sweep-tummy" x1="0" y1="0" x2="0" y2="1">
          <stop offset="0" stop-color="var(--tummy-top)"/>
          <stop offset="1" stop-color="var(--tummy-bottom)"/>
        </linearGradient>
      </defs>
      <path d="M175 0 C232 95 232 250 178 350 L260 350 L260 0 Z" fill="url(#sweep-tummy)"/>
    </svg>
    <div class="label-content">
      <h2 class="product-name">Tummy<br>Ease</h2>
      <p class="product-claim" style="top:128px"><span class="claim-lead">Oxygenating</span><span class="claim-detail">Colon Cleanse</span></p>
      <p class="supplement-pill" style="top:190px">Dietary Supplement</p>
      <p class="capsule-count">90 Vegetable Capsules</p>
    </div>
  </article>

  <article class="label label--blood">
    <div class="label-pattern" role="img" aria-label="Faint floral line pattern across the label"></div>
    <svg class="colour-sweep" viewBox="0 0 260 350" aria-hidden="true">
      <defs>
        <linearGradient id="sweep-blood" x1="0" y1="0" x2="0" y2="1">
          <stop offset="0" stop-color="var(--blood-top)"/>
          <stop offset="1" stop-color="var(--blood-bottom)"/>
        </linearGradient>
      </defs>
      <path d="M175 0 C232 95 232 250 178 350 L260 350 L260 0 Z" fill="url(#sweep-blood)"/>
    </svg>
    <div class="label-content">
      <h2 class="product-name">Blood<br>Sugar<br>Ease</h2>
      <p class="product-claim" style="top:170px"><span class="claim-lead">Supports Healthy</span><span class="claim-detail">Blood Glucose Levels</span></p>
      <p class="supplement-pill" style="top:223px">Dietary Supplement</p>
      <p class="capsule-count">60 Vegetable Capsules</p>
    </div>
  </article>

  <article class="label label--liver">
    <div class="label-pattern" role="img" aria-label="Faint floral line pattern across the label"></div>
    <svg class="colour-sweep" viewBox="0 0 260 350" aria-hidden="true">
      <defs>
        <linearGradient id="sweep-liver" x1="0" y1="0" x2="0" y2="1">
          <stop offset="0" stop-color="var(--liver-top)"/>
          <stop offset="1" stop-color="var(--liver-bottom)"/>
        </linearGradient>
      </defs>
      <path d="M175 0 C232 95 232 250 178 350 L260 350 L260 0 Z" fill="url(#sweep-liver)"/>
    </svg>
    <div class="label-content">
      <h2 class="product-name">Liver<br>Ease</h2>
      <p class="product-claim" style="top:124px"><span class="claim-lead">Rejuvenating</span><span class="claim-detail">Cleanse &amp; Detox<br>Formula</span></p>
      <p class="supplement-pill" style="top:200px">Dietary Supplement</p>
      <p class="capsule-count">120 Vegetable Capsules</p>
    </div>
  </article>

  <article class="label label--hormone">
    <div class="label-pattern" role="img" aria-label="Faint floral line pattern across the label"></div>
    <svg class="colour-sweep" viewBox="0 0 260 350" aria-hidden="true">
      <defs>
        <linearGradient id="sweep-hormone" x1="0" y1="0" x2="0" y2="1">
          <stop offset="0" stop-color="var(--hormone-top)"/>
          <stop offset="1" stop-color="var(--hormone-bottom)"/>
        </linearGradient>
      </defs>
      <path d="M175 0 C232 95 232 250 178 350 L260 350 L260 0 Z" fill="url(#sweep-hormone)"/>
    </svg>
    <div class="label-content">
      <h2 class="product-name">Hormone<br>Ease</h2>
      <p class="product-claim" style="top:128px"><span class="claim-lead">Supports Healthy</span><span class="claim-detail">Hormone Levels</span></p>
      <p class="supplement-pill" style="top:186px">Dietary Supplement</p>
      <p class="capsule-count">60 Vegetable Capsules</p>
    </div>
  </article>

</main>
</body>
</html>
```